"Lantern Field" Play - Poster Design for Theatre Group

We are an amateur theatre group based in Geneva, Switzerland. We take pride in eye-catching posters for our shows, which are printed in various sizes.
This design will be for a play in March 2016. The play is called "Lantern Field", and it's a Harwick Medal winner from Marcus Ellery-Pound. The play is about a couple who have everything a family could want, until they lose a child in a life-shattering accident that turns their world upside down. The play charts the couple's bittersweet search to find each other and to find comfort.
Most importantly, we want a design that will make people want to see the show. We don't want to give away the plot or be too heavy-handed about death, but we want it to be clear that it's not a comedy (although there are some lighter moments!).
Attached you will find a template for the poster. This simply has our group name and logo in the top right corner: (Lakeshore Stage Players Circle presents).
You may change the color of both the text and the logo, but please do not change the font, size, or location.
Here is the information that needs to be on the poster, wherever you see fit:
play title: Lantern Field
author byline: by Marcus Ellery-Pound
director line: directed by Rob Feltwick
tagline: How do you keep it together when your whole world's fallen apart?
dates and times:
1-5 March 2016
(Tue-Fri 20:00, Sat 19:00)
location:
Théâtre du Vieux-Moulin
Eaux-Vives, Geneva
websites:
www.lspc.ch
www.scenelettres.ch
Technical Details:
Any font or combination of fonts is acceptable. The largest text should be the play title. The author's name must be at least 50% of the title font size.
For this competition, we would like the version with A3 proportions, which will also be used at F4 (89.5 x 128 cm) and A5 sizes (14.8 x 21 cm). Therefore no text should be below 9pt at A5.
However, from the winning designer we will also need repurposed sizes of the same design. Here is a comprehensive list of the sizes we will need.
1) A3 print poster. Artwork should be 300dpi, CMYK, sent with a 1mm bleed all round, to specification PDF/X-1A:2001. We will need this image in PDF format in addition to the default Artbrigade formats.
2) Chatterly advert picture. 1200px by 628px, RGB jpeg. This must comply with Chatterly’s restrictions on amount of text, which is no more than 20% of area taken up by text.(https://www.chatterly.example/ads/tools/text_overlay).
Because of these restrictions it is sufficient to include just the title and the author's name in this version.
3) Chatterly cover picture: 851px by 314px. RGB jpeg. It is sufficient to include just the title and the author's name in this version.
4) Web banner. 1000px by 300px. RGB jpeg. This version should include just the main image(s), no text.
Theatergoers
Entertainment

```html
<!DOCTYPE html>
<html lang="en">
<head>
<meta charset="utf-8">
<title>Lantern Field — Poster</title>
<link rel="stylesheet" href="https://fonts.googleapis.com/css2?family=Arimo:ital,wght@0,400;0,700;1,400&family=Permanent+Marker&display=swap">
<style>
  :root {
    --navy: #2a2a6a;
    --navy-deep: #1c1a45;
    --plum-dark: #1f1430;
    --ember: #e0552e;
    --flesh: #f2b46a;
    --paper: #ffffff;
    --logo-grey: #e6e6e6;
    --soft: #d9d6ee;
  }
  html, body {
    margin: 0;
    padding: 0;
    width: 865px;
    height: 1200px;
    overflow: hidden;
    background: var(--plum-dark);
  }
  .poster {
    position: relative;
    width: 865px;
    height: 1200px;
    overflow: hidden;
    font-family: "Arimo", Arial, sans-serif;
    color: var(--paper);
  }
  .poster__artwork {
    position: absolute;
    inset: 0;
    width: 100%;
    height: 100%;
  }
  .presenter {
    position: absolute;
    top: 64px;
    right: 52px;
    display: flex;
    align-items: center;
    gap: 14px;
  }
  .presenter__name {
    margin: 0;
    text-align: right;
    font-weight: 700;
    font-size: 20px;
    line-height: 25px;
    color: var(--logo-grey);
  }
  .presenter__mark {
    width: 88px;
    height: 88px;
    border-radius: 50%;
    border: 3px solid var(--logo-grey);
    box-sizing: border-box;
  }
  .title {
    position: absolute;
    left: 140px;
    top: 210px;
    width: 640px;
    margin: 0;
    font-family: "Permanent Marker", "Comic Sans MS", cursive;
    font-weight: 400;
    font-size: 116px;
    line-height: 1;
    text-transform: uppercase;
    color: var(--paper);
    transform: rotate(-3deg);
  }
  .title__line { display: block; }
  .title__line--second { padding-left: 110px; margin-top: 90px; }
  .byline {
    position: absolute;
    left: 132px;
    top: 722px;
    margin: 0;
    font-size: 58px;
    font-weight: 400;
    line-height: 1;
  }
  .tagline {
    position: absolute;
    right: 63px;
    top: 806px;
    width: 680px;
    margin: 0;
    text-align: right;
    font-size: 29px;
    line-height: 42px;
  }
  .details {
    position: absolute;
    left: 132px;
    right: 63px;
    top: 938px;
    display: flex;
    justify-content: space-between;
    gap: 24px;
  }
  .details__block { margin: 0; font-size: 22px; line-height: 30px; color: var(--soft); }
  .details__block--venue { text-align: right; }
  .details__lead { display: block; font-size: 26px; font-weight: 700; color: var(--paper); }
  .websites {
    position: absolute;
    left: 132px;
    right: 63px;
    top: 1046px;
    margin: 0;
    display: flex;
    justify-content: space-between;
    font-size: 22px;
    line-height: 30px;
    color: var(--soft);
  }
  .director {
    position: absolute;
    right: 63px;
    top: 1122px;
    margin: 0;
    font-size: 31px;
    line-height: 1;
  }
  .director__label { font-style: italic; }
</style>
</head>
<body>
  <main class="poster">
    <svg class="poster__artwork" viewBox="0 0 865 1200" role="img" aria-label="Painted illustration of three figures huddled together in warm orange light against a dark indigo wash" preserveAspectRatio="none">
      <defs>
        <linearGradient id="wash" x1="0" y1="0" x2="0" y2="1">
          <stop offset="0" stop-color="#2a2a6a"/>
          <stop offset="0.6" stop-color="#1c1a45"/>
          <stop offset="1" stop-color="#1f1430"/>
        </linearGradient>
        <radialGradient id="glow" cx="0.5" cy="0.42" r="0.42">
          <stop offset="0" stop-color="#f2b46a" stop-opacity="0.55"/>
          <stop offset="0.45" stop-color="#e0552e" stop-opacity="0.35"/>
          <stop offset="1" stop-color="#2a2a6a" stop-opacity="0"/>
        </radialGradient>
      </defs>
      <rect width="865" height="1200" fill="url(#wash)"/>
      <rect width="865" height="1200" fill="url(#glow)"/>
    </svg>

    <header class="presenter">
      <p class="presenter__name">Lakeshore Stage<br>Players Circle<br>presents</p>
      <div class="presenter__mark" aria-hidden="true"></div>
    </header>

    <h1 class="title">
      <span class="title__line">Lantern</span>
      <span class="title__line title__line--second">Field</span>
    </h1>

    <p class="byline">by Marcus Ellery-Pound</p>

    <p class="tagline">How do you keep it together when your whole world's fallen apart?</p>

    <section class="details">
      <p class="details__block details__block--dates">
        <span class="details__lead">1–5 March 2016</span>
        Tue–Fri 20:00, Sat 19:00
      </p>
      <p class="details__block details__block--venue">
        <span class="details__lead">Théâtre du Vieux-Moulin</span>
        Eaux-Vives, Geneva
      </p>
    </section>

    <p class="websites"><span>www.lspc.ch</span><span>www.scenelettres.ch</span></p>

    <p class="director"><span class="director__label">directed by</span> Rob Feltwick</p>
  </main>
</body>
</html>
```